Clean & Inspiring Web Design Project

Quillstone Makers, LLC (also known as Q9-Makers) is a company which provides 3D printing services and products. The emphasis is on making these products and services available to the mass-market - customers and users who may or may not have prior experience with 3D printing and/or rapid prototyping technologies. We are a start-up company, looking to build a clean and creativity inspiring brand - our site must encourage visitor to engage and make something. Our aim is to help take mere ideas and turn them into tangible items. We want to show a fusion of ideas (e.g. pencil sketches on graph paper) with design tools (e.g. CAD and drafting software) and rapid prototyping (e.g. TurnKit 3D printers, Stereolithography Machines, etc.). We would like the website to appear professional but at the same time easy to navigate and a good balance between text and pictures. The final design should inspire customers to nurture their ideas into real products and communicate our services to our customers. Our site should have the feel of a vibrant social community with the added benefit of tangible physical creations.

Target Market(s)

People with great ideas that need to be designed into a real product

Industry/Entity Type

Printing

Requirements
Must have
• - Website design should include 2 layouts - one for a "landing page" and one for a "content page"
- Website design must incorporate attached company logo (or derivative of this logo)
- Website design should incorporate the menu options shown in the attached PDF UI concept (UI does not necessarily need to look like the provided concept, just include all the clickable elements)
- Website design must portray an innovative and cooperative design environment with a look-and-feel that appeals to both amateur and professional designers.
- Please include pictures, illustrations and photographs (as needed) related to 3D printing, CAD design, conventional drafting, engineering and manufacturing industries.
- Design should support scaling to multiple screen sizes, from tablet computers (e.g. eSlate) to very large screen PCs.
- Design should include Username & Password fields for login or a button to pull up a login popup.
Nice to have
• - Website design could include "Invent", "Make", "Produce" and "Buy" options that slowly cycle through - with appropriate photos / graphics. These "menu options" would also be mouse-over enabled to switch into the appropriate context as the cursor enters that region (e.g. mouse over the "Invent" text would bring up page 2, etc.). (See attached Original UI Thoughts)
Should not have
• Requirements - Should Not Have:
- Website design should not portray a service that is very expensive or complicated - we are a reasonably priced service meant to be friendly with amateur inventors
- Website design should not be overly complicated - please keep it reasonably simple
- Website design should not be overly trendy
- Website design should not use more than 2 font styles, gaudy fonts, etc.
- Website design should not be "campy" or "tacky" - playful is ok, but please keep it elegant
- Website design should not be overly masculine or feminine - we will have both women and men as customers

```html
<!DOCTYPE html>
<html lang="en">
<head>
<meta charset="utf-8">
<title>Quillstone Makers — Why Q9</title>
<link rel="stylesheet" href="https://fonts.googleapis.com/css2?family=Arvo:wght@400;700&family=Arimo:wght@400;700&display=swap">
<style>
:root{
  --brand-blue:#1f6fa8;
  --nav-blue:#3b95cf;
  --heading-blue:#1d6593;
  --accent-red:#ff2a1f;
  --accent-red-dark:#e3160f;
  --text-dark:#1e1e1e;
  --text-muted:#8c8c8c;
  --header-top:#f7f7f7;
  --header-bottom:#dcdcdc;
  --band-grey:#d0d0d0;
  --footer-dark:#353535;
  --footer-text:#e6e6e6;
  --white:#ffffff;
}
*{box-sizing:border-box;margin:0;padding:0}
html,body{width:1200px;height:658px;overflow:hidden;background:var(--white)}
body{font-family:"Arimo",Arial,sans-serif;color:var(--text-dark);position:relative}
a{color:inherit;text-decoration:none}

/* Header */
.site-header{position:absolute;left:0;top:0;width:1200px;height:69px;
  background:linear-gradient(var(--header-top),var(--header-bottom));border-bottom:1px solid #c9c9c9}
.brand{position:absolute;left:177px;top:10px;display:flex;align-items:center;gap:8px}
.brand-mark{width:46px;height:50px;background:var(--brand-blue);border-radius:5px;
  display:flex;align-items:center;justify-content:center;color:var(--white);
  font-family:"Arvo",serif;font-weight:700;font-size:17px}
.brand-tagline{font-family:"Arvo",serif;font-size:14px;line-height:21px;color:#333;margin-left:2px}

.why-tab{position:absolute;left:499px;top:0;width:65px;height:95px}
.why-tab svg{position:absolute;left:0;top:0}
.why-tab span{position:absolute;left:0;top:26px;width:65px;text-align:center;
  font-family:"Arvo",serif;font-size:14px;color:var(--white)}

.main-nav a{position:absolute;top:26px;font-family:"Arvo",serif;font-size:14px;color:var(--nav-blue)}
.nav-dreamer{left:577px}.nav-maker{left:669px}.nav-producer{left:740px}

.shop-box{position:absolute;left:842px;top:23px;width:181px;height:24px;
  border:1px solid #c4c4c4;background:#f2f2f2;display:flex;align-items:center;font-size:10px;color:#444}
.shop-box .shop{padding:0 6px;border-right:1px solid #c4c4c4;height:100%;display:flex;align-items:center}
.shop-box .cart{display:flex;align-items:center;gap:4px;padding-left:6px}

/* Sub navigation */
.sub-nav{position:absolute;left:177px;top:91px;display:flex;gap:0;font-size:10.5px}
.sub-nav a{height:19px;line-height:19px;padding:0 4px;margin-right:5px;color:var(--text-muted)}
.sub-nav .active{background:var(--accent-red);color:var(--white)}
.sub-nav .current{color:var(--text-dark)}

/* Content */
.intro{position:absolute;left:183px;top:160px;width:466px}
.intro h1{font-family:"Arvo",serif;font-weight:400;font-size:19.5px;line-height:29px;color:var(--heading-blue);margin-bottom:8px}
.intro p{font-size:10.2px;line-height:21.1px;margin-bottom:21px}

.team{position:absolute;left:777px;top:158px;width:142px;text-align:center}
.team-label{font-size:12px;color:#333;margin-bottom:15px;padding-left:0}
.bios-button{display:block;height:49px;line-height:45px;border:2px solid #e3d5d5;
  background:linear-gradient(var(--accent-red),var(--accent-red-dark));color:var(--white);
  font-weight:700;font-size:19px}

.product-photo{position:absolute;left:706px;top:290px;width:279px;height:198px;border-radius:40px;
  background:radial-gradient(ellipse at 45% 50%,#efede6 0%,#dcd9cf 55%,#ffffff 100%)}

/* Footer band */
.footer-band{position:absolute;left:0;top:531px;width:1200px;height:42px;background:var(--band-grey)}
.follow{position:absolute;left:184px;top:15px;font-size:10.5px;display:flex;align-items:center;gap:5px}
.follow .label{margin-right:8px}
.social{width:20px;height:20px;border-radius:3px;background:#8a8a8a}
.social-mail{background:#e9d7b0;display:flex;align-items:center;justify-content:center}
.footer-links{position:absolute;right:182px;top:15px;font-size:10.5px}

/* Dark footer */
.footer-dark{position:absolute;left:0;top:573px;width:1200px;height:85px;background:var(--footer-dark);color:var(--footer-text)}
.footer-mark{position:absolute;left:186px;top:16px;width:46px;height:54px;border-radius:5px;background:#777;
  display:flex;align-items:center;justify-content:center;font-family:"Arvo",serif;font-weight:700;font-size:16px;color:#e6e6e6}
.footer-name{position:absolute;left:246px;top:22px;font-family:"Arvo",serif;font-size:14px}
.footer-tag{position:absolute;left:247px;top:46px;font-family:"Arvo",serif;font-size:11.5px}
.copyright{position:absolute;right:179px;top:25px;font-size:10.5px}
.legal{position:absolute;left:750px;top:47px;width:272px;font-size:10.5px;display:flex;justify-content:space-between}
</style>
</head>
<body>

<header class="site-header">
  <div class="brand">
    <div class="brand-mark">Q9</div>
    <div class="brand-tagline">What you want.<br>Now!</div>
  </div>
  <nav class="main-nav">
    <a class="why-tab" href="#">
      <svg width="65" height="95" viewBox="0 0 65 95"><polygon points="0,0 65,0 65,70 32.5,95 0,70" fill="#ff2a1f"/></svg>
      <span>WHY Q9</span>
    </a>
    <a class="nav-dreamer" href="#">DREAMER</a>
    <a class="nav-maker" href="#">MAKER</a>
    <a class="nav-producer" href="#">PRODUCER</a>
  </nav>
  <div class="shop-box">
    <a class="shop" href="#">SHOP</a>
    <a class="cart" href="#">
      <svg width="14" height="12" viewBox="0 0 14 12"><path d="M0 1h3l2 7h7l2-5H4" fill="none" stroke="#555" stroke-width="1.3"/><circle cx="6" cy="10.5" r="1.2" fill="#555"/><circle cx="11" cy="10.5" r="1.2" fill="#555"/></svg>
      your cart 0 item selected
    </a>
  </div>
</header>

<nav class="sub-nav">
  <a class="active" href="#">ABOUT Q9</a>
  <a class="current" href="#">DREAM</a>
  <a href="#">MAKE</a>
  <a href="#">PRODUCE</a>
  <a href="#">SELL</a>
</nav>

<main>
  <section class="intro">
    <h1>Lorem ipsum dolor sit amet, consectetur adipiscing elit.</h1>
    <p>Suspendisse dapibus pellentesque urna vitae cursus. Class aptent taciti sociosqu ad litora torquent per conubia nostra, per inceptos himenaeos. Maecenas pharetra convallis enim, a venenatis leo sceleris-que nec. Pellentesque habitant morbi tristique senectus et netus et malesuada fames ac turpis egestas. Cras tristique aliquam eros nec congue. Nam tempus, eros vitae volutpat consectetur, purus nunc vulputate turpis, lobortis eleifend mauris nisi a nisl. Praesent consequat fermentum malesuada. Pellentesque habitant morbi tristique senectus et netus et malesuada fames ac turpis egestas. Sus-pendisse potenti. Pellentesque in nunc est.</p>
    <p>Praesent blandit aliquam dictum. Morbi auctor ante eu ipsum hendrerit sagittis. Praesent porttitor, lectus vitae iaculis pulvinar, ligula erat accumsan dui, non congue risus turpis ac lorem. Nam dignissim, lectus molestie sagittis porttitor, sem lectus mattis turpis, eget faucibus metus odio eu risus. Nulla ut elementum nisi. Praesent tempor tellus eget tellus luctus quis bibendum urna dignissim. Cras porta nunc vel ante dictum volutpat. Quisque at tortor id nunc bibendum dapibus.</p>
  </section>

  <aside class="team">
    <div class="team-label">TEAM Q9</div>
    <a class="bios-button" href="#">BIOS</a>
  </aside>

  <div class="product-photo" role="img" aria-label="Photo of a white 3D-printed cylindrical part with ribbed rings and a perforated shell"></div>
</main>

<footer>
  <div class="footer-band">
    <div class="follow">
      <span class="label">Follow us</span>
      <a class="social" href="#" aria-label="Social network 1"></a>
      <a class="social" href="#" aria-label="Video channel"></a>
      <a class="social" href="#" aria-label="Social network 2"></a>
      <a class="social" href="#" aria-label="Social network 3"></a>
      <a class="social social-mail" href="#" aria-label="Email">
        <svg width="16" height="12" viewBox="0 0 16 12"><rect x="0.5" y="0.5" width="15" height="11" fill="#fff4dc" stroke="#b48a4a"/><path d="M0.5 0.5 8 7 15.5 0.5" fill="none" stroke="#b48a4a"/></svg>
      </a>
    </div>
    <nav class="footer-links">HOME | CONTACT | FRANCHISE | DISTRIBUTORS | CART</nav>
  </div>
  <div class="footer-dark">
    <div class="footer-mark">Q9</div>
    <div class="footer-name">Quillstone Makers</div>
    <div class="footer-tag">What you want... NOW!</div>
    <div class="copyright">© Copyright Quillstone Makers, 2012 All Rights Reserved</div>
    <div class="legal"><span>Privacy Policy &nbsp;|&nbsp; Terms of Service</span><span>M3</span></div>
  </div>
</footer>

</body>
</html>
```